Vodka label, brand name: LATE BIRCH

We are looking for a vodka label design, which will print on paper or plastic (not a bottle printing)

We are small distilling company: Ferncliff Distillery. Located in Toronto, Canada. Our business is small batches of handcrafted very smooth vodka production. 40% abv. Made from cane sugar and spring water.

Our audience pretty mach everyone who consume vodka/alcohol, we are not targeting any specific group.

Back label should have barcode, government warning and this text:

Our vodka is handmade in small batches to the highest standards befitting the true vodka perfectionist. We use silk filtering process for exceptional purity, clarity, and smoothness. It is distilled 6 times from the finest organic cane sugar using only the best Canadian spring water. Discover the smooth, clear taste for yourself.
Distilled and Bottled by
Ferncliff Distillery Inc.
Toronto, Canada

Government Warning: In accordance to the Surgeon General, women should not drink alcoholic beverages during pregnancy because of the risk of birth defects. Consumption of alcoholic beverages impairs your ability to drive a car or operate machinery and may cause health problems.

Size of the bottle as follows (see example in the attachment) :
Volume: 750ml
Total height: 330mm
Body diameter: 77mm
Closure: Bar Top
Silver synthetic cork

Target Market(s)

Colors

Designer to choose colors to be used in the design.

Requirements
Must have
• Incorporate the name: LATE BIRCH
• Incorporate: DISTILLED FROM ORGANIC CANE SUGAR
• Back bottle label should have barcode, government warning and this text:
• Our vodka is handmade in small batches to the highest standards befitting the true vodka perfectionist. We use silk filtering process for exceptional purity, clarity, and smoothness. It is distilled 6 times from the finest organic cane sugar using only the best Canadian spring water. Discover the smooth, clear taste for yourself.
• Distilled and Bottleb by
• Ferncliff Distillery Inc.
• Toronto, Canada
• Government Warning: In accordance to the Surgeon General, women should not drink alcoholic beverages during pregnancy because of the risk of birth defects. Consumption of alcoholic beverages impairs your ability to drive a car or operate machinery and may cause health problems.
Nice to have
• 1) To show in wording or design it was Handmade
• 2) To show in wording or design it was made with Natural Spring Water
• To show in wording or design it was made in small batches
• 3) To show in wording or design it was made local in Toronto, Canada
• "The Six" "The 6ix"- is the nick name of city of Toronto that's just for designer to consider and not mandatory to implement on design
Should not have
• We try to lower cost of printing , so design should be for digital printing without Gold, Silver or any other color which requires foil application on label and will increase cost of printing.
• No copy paste from internet images. Such designs will be ignored and reported to website admin. Authentic design work only.
• Please try not to use clock or any related to that images. Its nothing to do with clock, its too naive to show 6 pm on the watches in your design. Its could be time of the day (evening), after work, the six as nick name of Toronto. But not clock or watches .

```html
<!DOCTYPE html>
<html lang="en">
<head>
<meta charset="utf-8">
<title>Late Birch Vodka – Labels</title>
<link href="https://fonts.googleapis.com/css2?family=Josefin+Sans:wght@300;400;600&family=Jost:wght@300;400;500&display=swap" rel="stylesheet">
<style>
  :root{
    --backdrop:#ececec;
    --paper:#ffffff;
    --ink:#1c1c1f;
    --ink-soft:#55565c;
    --navy:#1a3683;
    --navy-deep:#142b6c;
    --mist:#c7d1e6;
    --on-navy:#ffffff;
    --code-frame:#b9bcc4;
  }
  *{box-sizing:border-box;margin:0;padding:0}
  html,body{width:1200px;height:1200px;overflow:hidden}
  body{
    background:var(--backdrop);
    font-family:"Jost",sans-serif;
    color:var(--ink);
    display:flex;align-items:center;justify-content:center;gap:80px;
  }
  .label{
    width:440px;height:815px;background:var(--paper);
    position:relative;overflow:hidden;
    box-shadow:0 6px 24px rgba(0,0,0,.08);
  }
  /* front label */
  .label--front{
    background:linear-gradient(to bottom,var(--paper) 0%,var(--paper) 57%,var(--mist) 65%,var(--navy) 75%,var(--navy-deep) 100%);
    text-align:center;
  }
  .maker{
    position:absolute;top:58px;left:0;right:0;
    font-family:"Josefin Sans",sans-serif;font-weight:600;font-size:26px;letter-spacing:.5px;
  }
  .maker__mark{display:inline-block;width:11px;height:11px;border:2px solid var(--ink);border-radius:50%;margin-right:8px;vertical-align:3px}
  .name-top{
    position:absolute;top:165px;left:0;right:0;
    font-family:"Josefin Sans",sans-serif;font-weight:400;font-size:92px;line-height:1;letter-spacing:1px;
  }
  .name-row{
    position:absolute;top:262px;left:28px;right:28px;height:210px;
    display:flex;align-items:center;justify-content:center;gap:12px;
  }
  .night-emblem{width:90px;height:200px;border-radius:45px;background:radial-gradient(circle at 40% 40%,#f4f5f8,#d5d9e3)}
  .name-bottom{
    font-family:"Josefin Sans",sans-serif;font-weight:300;font-size:92px;line-height:1;letter-spacing:2px;
  }
  .spirit{
    position:absolute;top:490px;left:0;right:0;
    font-family:"Josefin Sans",sans-serif;font-weight:300;font-size:40px;letter-spacing:24px;padding-left:24px;
  }
  .handmade{
    position:absolute;top:538px;left:0;right:0;
    font-size:13px;letter-spacing:8px;padding-left:8px;
  }
  .origin{
    position:absolute;top:632px;left:0;right:0;color:var(--on-navy);
    font-family:"Josefin Sans",sans-serif;font-size:19px;letter-spacing:2px;line-height:1.55;
  }
  .origin__dot{display:inline-block;width:10px;height:10px;background:var(--on-navy);transform:rotate(45deg);margin:0 10px 2px}
  .source{
    position:absolute;top:702px;left:14px;right:14px;color:var(--on-navy);
    border-top:1px solid var(--on-navy);border-bottom:1px solid var(--on-navy);
    font-family:"Josefin Sans",sans-serif;font-size:15.5px;letter-spacing:.3px;padding:4px 0 2px;
  }
  .specs{
    position:absolute;top:742px;left:20px;right:20px;color:var(--on-navy);
    display:flex;justify-content:space-between;font-size:24px;font-weight:300;
  }
  /* back label */
  .back-copy{position:absolute;left:26px;right:26px;bottom:34px}
  .story{font-size:14.5px;line-height:1.5;color:var(--ink)}
  .story strong{font-weight:500}
  .legal{margin-top:20px;display:flex;gap:16px;align-items:flex-start}
  .legal__text{flex:1}
  .bottler{font-size:12.5px;line-height:1.5;text-transform:uppercase;letter-spacing:.3px}
  .warning{margin-top:16px;font-size:11.5px;line-height:1.55;text-transform:uppercase;letter-spacing:.2px;color:var(--ink-soft)}
  .barcode-area{
    width:58px;height:130px;flex:none;margin-top:2px;
    background:var(--paper);border:1px solid var(--code-frame);
  }
</style>
</head>
<body>
  <section class="label label--front" aria-label="Front label">
    <div class="maker"><span class="maker__mark"></span>Ferncliff Distillery</div>
    <div class="name-top">LATE</div>
    <div class="name-row">
      <div class="night-emblem" role="img" aria-label="Crescent moon and stars illustration"></div>
      <div class="name-bottom">BIRCH</div>
    </div>
    <div class="spirit">VODKA</div>
    <div class="handmade">HANDMADE</div>
    <div class="origin">MADE IN<span class="origin__dot"></span>FABRIQUÉ AU<br>TORONTO, CANADA</div>
    <div class="source">DISTILLED FROM FINEST ORGANIC CANE SUGAR</div>
    <div class="specs"><span>40% abv.</span><span>750ml</span></div>
  </section>

  <section class="label label--back" aria-label="Back label">
    <div class="back-copy">
      <p class="story">Our vodka is handmade in small batches to the highest standards befitting the true vodka perfectionist. We use silk filtering process for exceptional purity, clarity, and smoothness. It is distilled 6 times from the finest organic cane sugar using only the best Canadian spring water. <strong>Discover the smooth, clear taste for yourself.</strong></p>
      <div class="legal">
        <div class="legal__text">
          <p class="bottler">Distilled and bottled by<br>Ferncliff Distillery Inc. Toronto, Canada</p>
          <p class="warning">Government warning: (1) According to the Surgeon General, women should not drink alcoholic beverages during pregnancy because of the risk of birth defects. (2) Consumption of alcoholic beverages impairs your ability to drive a car or operate machinery, and may cause health problems.</p>
        </div>
        <div class="barcode-area" role="img" aria-label="Space reserved for the product barcode"></div>
      </div>
    </div>
  </section>
</body>
</html>
```